Your Harbor Agent Website Design

Creative Brief: Website Design for Your Harbor Agent
- Project Overview: Design a website for our new brand, "Your Harbor Agent". Your Harbor Agent is a service that matches clients with the perfect realtor. The primary function of this site is to serve as a lead generation hub, to generate leads of people who are looking to either buy or sell their house and need a great realtor. The site needs to have a very clean, modern design using sites like Tallyquest, Brickwell, Lantern, and Vexomill as an example. The site also needs to have a primary lead capture capability through a multi-step form or questionnaire that indicates if they are buying or selling, and depending on that selection, creates two different flows.

Target Audience:
- Homebuyers and sellers in the Denver area
- Individuals looking for high-quality realtor services
- Users seeking a seamless and professional online & home buying/selling experience

Objectives:
- Create a visually appealing, modern website with a strong emphasis on lead generation.
- Design advanced, multi-step forms for efficient lead capture.
- Ensure the website is user-friendly and optimized for both desktop and mobile devices.

Pages to Design:
Home Page:
- Engaging hero section with a clear call to action and the ability to enter the form flow
- Brief introduction to Your Harbor Agent and its unique value proposition
- Key features & benefits of being matched with a realtor by Your Harbor Agent
- Testimonials and success stories
- Lead capture form

About Page:
- Overview of Your Harbor Agent’s mission and values
- Professional and trust-building imagery

How it Works Page:
- Step-by-step explanation of the matching process (complete the form and we will match you with a realtor)
- Visual aids (icons, graphics) to simplify complex information
- Customer journey map from inquiry to successful match & sale of home
- Lead capture form

Contact Us Page:
- Simple and accessible contact form
- Contact details
- Call to action for immediate inquiries

Blog Template:
- Clean, easy-to-read layout for blog posts, primarily location/neighborhood guides as well as standard blogs
- Sidebar for recent posts, categories, and tags
- Social sharing buttons
- Lead capture form embedded within blog posts

Design Style:
- Modern and professional with a focus on usability
- Clean lines and intuitive navigation
- Use of curved corners and minimal straight lines for a sleek look
- Incorporation of graphic design elements, potentially including 3D and isomorphic design
- Inspired by sites like Tallyquest, Brickwell, Lantern, and Vexomill
Consistent color scheme and typography

Visual References:
- Tallyquest: For its professional and corporate look
- Brickwell and Lantern: For their user-friendly interfaces and modern design
- Vexomill: For its clean and functional layout

Target Market(s)

- Homebuyers and sellers in the Denver area, Individuals looking for high-quality realtor services, Users seeking a seamless and professional home buying/selling experience

Industry/Entity Type

Real Estate

Number of Pages Required

5+ page

Requirements
Must have
• Fully designed website with lead capture functionality based on brief
Nice to have
• Designed in Figma, Starting / Placeholder copy

```html
<!DOCTYPE html>
<html lang="en">
<head>
<meta charset="UTF-8">
<title>About Us – Your Harbor Agent</title>
<link href="https://fonts.googleapis.com/css2?family=Outfit:wght@300;400;500;600&display=swap" rel="stylesheet">
<style>
:root{
  --coral:#ee6352;
  --coral-soft:#fcd3cc;
  --cream:#fbf2e9;
  --ink:#1f1a17;
  --muted:#7a716b;
  --brown:#2a1a05;
  --white:#ffffff;
}
*{box-sizing:border-box;margin:0;padding:0}
html,body{width:1200px;height:3311px;overflow:hidden}
body{font-family:"Outfit",sans-serif;background:var(--cream);color:var(--ink);position:relative}
a{color:inherit;text-decoration:none}

.site-nav{position:absolute;top:0;left:0;width:1200px;height:59px;background:var(--white);display:flex;align-items:center;justify-content:space-between;padding:0 53px}
.brand{font-family:"Outfit",sans-serif;font-weight:500;font-size:20px;color:var(--coral)}
.nav-links{display:flex;align-items:center;gap:28px;font-size:13px}
.nav-links .active{font-weight:600}
.btn-pill{background:var(--coral);color:var(--white);border-radius:20px;padding:9px 18px;font-size:13px}

.mission{position:absolute;top:59px;left:0;width:1200px;height:300px;background:var(--coral);color:var(--white)}
.mission h1{position:absolute;left:53px;top:92px;font-size:41px;font-weight:500}
.mission p{position:absolute;left:634px;top:94px;width:500px;font-size:14.5px;line-height:22.5px;font-weight:300}

.impact h2,.values h2,.team h2{font-size:39px;font-weight:500;letter-spacing:-.3px}
.impact{position:absolute;top:452px;left:53px;width:1094px}
.impact h2{position:absolute;top:98px;left:0}
.impact .lead{position:absolute;top:164px;left:0;width:520px;font-size:14.5px;line-height:22.5px}
.stats{position:absolute;top:264px;left:0;display:grid;grid-template-columns:266px 266px;row-gap:36px}
.stat-num{font-size:39px;font-weight:500;color:var(--coral);line-height:1}
.stat-label{font-size:12.5px;color:var(--muted);margin-top:12px}
.photo{border-radius:18px}
.impact .photo{position:absolute;left:581px;top:0;width:513px;height:534px;background:linear-gradient(160deg,#f1d9cc 0%,#d98d86 45%,#a5524a 70%,#6f7c4a 100%)}

.values{position:absolute;top:1170px;left:53px;width:1094px}
.values h2{text-align:center}
.values .lead{width:560px;margin:18px auto 0;text-align:center;font-size:14.5px;line-height:22.5px}
.value-grid{position:absolute;top:211px;left:0;display:grid;grid-template-columns:266px 266px;row-gap:34px}
.value-icon{width:50px;height:50px;border-radius:12px;background:var(--coral-soft);display:flex;align-items:center;justify-content:center}
.value h3{font-size:20px;font-weight:500;line-height:28px;margin-top:18px;width:200px}
.value p{font-size:12.5px;line-height:20px;margin-top:14px;width:256px}
.values .photo{position:absolute;left:581px;top:208px;width:513px;height:532px;background:linear-gradient(135deg,#7a3a34 0%,#5b4742 40%,#8a7463 70%,#3b3532 100%)}
.play{position:absolute;left:233px;top:243px;width:46px;height:46px;border-radius:50%;background:var(--white);display:flex;align-items:center;justify-content:center}

.team{position:absolute;top:2070px;left:53px;width:1094px}
.team .lead{font-size:14.5px;margin-top:20px}
.team-grid{position:absolute;top:159px;left:0;display:grid;grid-template-columns:573px 521px;row-gap:54px}
.member{display:flex;gap:27px}
.member .portrait{width:246px;height:240px;border-radius:16px;flex:none;background:linear-gradient(160deg,#e6e1da,#b9ada2)}
.member h3{font-size:16.5px;font-weight:500;margin-top:4px}
.member .role{font-size:14.5px;color:var(--muted);margin-top:6px;font-weight:300}
.member p{font-size:12.5px;line-height:20px;margin-top:14px;width:240px}
.socials{display:flex;gap:16px;margin-top:18px}
.socials span{width:16px;height:16px;border:1.6px solid var(--coral);border-radius:4px}
.socials span.round{border-radius:50%}

.site-footer{position:absolute;top:2857px;left:0;width:1200px;height:454px;background:var(--brown);color:var(--white)}
.site-footer .brand{position:absolute;left:53px;top:79px;color:var(--white)}
.quick{position:absolute;left:355px;top:75px}
.quick h4,.subscribe h4{font-size:13px;font-weight:500}
.quick ul{list-style:none;margin-top:24px;font-size:11.5px;line-height:31px}
.subscribe{position:absolute;left:730px;top:75px;width:417px}
.subscribe p{font-size:12.5px;margin-top:22px}
.form-row{display:flex;gap:12px;margin-top:18px}
.email{width:306px;height:41px;border-radius:8px;background:var(--white);color:#9a928b;font-size:12px;padding:12px 11px}
.btn-outline{width:100px;height:41px;border:1px solid var(--white);border-radius:21px;font-size:13px;display:flex;align-items:center;justify-content:center}
.fine{font-size:9px;line-height:14px;margin-top:12px}
.fine u,.legal u{text-decoration:underline}
.rule{position:absolute;left:53px;top:339px;width:1094px;height:1px;background:rgba(255,255,255,.4)}
.legal{position:absolute;left:53px;top:369px;font-size:11px;display:flex;gap:22px}
.foot-social{position:absolute;right:53px;top:366px;display:flex;gap:14px}
.foot-social span{width:16px;height:16px;background:var(--white);border-radius:50%}
.foot-social span.sq{border-radius:3px}
</style>
</head>
<body>

<nav class="site-nav">
  <a class="brand" href="#">Your Harbor Agent</a>
  <div class="nav-links">
    <a class="active" href="#">About Us</a>
    <a href="#">How it Works</a>
    <a href="#">Blog</a>
    <a class="btn-pill" href="#">Contact Us</a>
  </div>
</nav>

<header class="mission">
  <h1>Our Mission</h1>
  <p>At Your Harbor Agent, our mission is to revolutionize the real estate experience by seamlessly connecting clients with the ideal realtors for their unique needs. We aim to simplify the process of buying and selling homes in Denver, ensuring that our clients receive the highest level of service, expertise, and satisfaction.</p>
</header>

<section class="impact">
  <h2>Impact by the Numbers</h2>
  <p class="lead">At Your Harbor Agent, we pride ourselves on the positive impact we've made in the Denver real estate market. Here's a snapshot of our success by the numbers:</p>
  <div class="stats">
    <div><div class="stat-num">500+</div><div class="stat-label">Successful Matches</div></div>
    <div><div class="stat-num">95%</div><div class="stat-label">Client Satisfaction Rate</div></div>
    <div><div class="stat-num">$10 Million+</div><div class="stat-label">Value of Properties Sold</div></div>
    <div><div class="stat-num">40+</div><div class="stat-label">Neighborhoods Served</div></div>
  </div>
  <div class="photo" role="img" aria-label="Photo of a row of colorful townhouses along a tree-lined street"></div>
</section>

<section class="values">
  <h2>Our Values</h2>
  <p class="lead">At Your Harbor Agent, we are passionate about making real estate connections easy, effective, and rewarding. Our mission and values guide us in delivering exceptional service and creating lasting relationships with our clients.</p>
  <div class="value-grid">
    <div class="value">
      <div class="value-icon"><svg width="24" height="24" viewBox="0 0 24 24" fill="none" stroke="#ee6352" stroke-width="1.5"><circle cx="8" cy="7" r="3"/><circle cx="16" cy="7" r="3"/><path d="M3 20v-3a4 4 0 0 1 4-4h2M21 20v-3a4 4 0 0 0-4-4h-2"/></svg></div>
      <h3>Client-Centric Approach</h3>
      <p>Our clients are at the heart of everything we do. We listen to their needs, understand their goals, and tailor our services to provide a personalized and stress-free real estate experience.</p>
    </div>
    <div class="value">
      <div class="value-icon"><svg width="24" height="24" viewBox="0 0 24 24" fill="none" stroke="#ee6352" stroke-width="1.5"><path d="M12 3l7 3v6c0 4-3 7-7 9-4-2-7-5-7-9V6z"/><path d="M9 12l2 2 4-4"/></svg></div>
      <h3>Integrity and Transparency</h3>
      <p>We believe in conducting our business with the utmost integrity and transparency. Our clients can trust that we operate with honesty and accountability, throughout the entire process.</p>
    </div>
    <div class="value">
      <div class="value-icon"><svg width="24" height="24" viewBox="0 0 24 24" fill="none" stroke="#ee6352" stroke-width="1.5"><circle cx="12" cy="9" r="5"/><path d="M9 13l-2 8 5-2 5 2-2-8"/></svg></div>
      <h3>Excellence and Professionalism</h3>
      <p>Our network of realtors consists of top-performing professionals who are committed to excellence. They bring extensive knowledge, experience, and dedication to every client interaction, ensuring the best possible outcomes.</p>
    </div>
    <div class="value">
      <div class="value-icon"><svg width="24" height="24" viewBox="0 0 24 24" fill="none" stroke="#ee6352" stroke-width="1.5"><path d="M14 4c3-1 6-1 6-1s0 3-1 6l-7 7-5-5z"/><path d="M7 11l-3 1 2 2M13 17l-1 3-2-2M5 19l3-3"/></svg></div>
      <h3>Innovation and Efficiency</h3>
      <p>We leverage innovative technology and streamlined processes to make finding the perfect realtor quick and easy. Our efficient matching system saves our clients time and effort, allowing them to focus on their real estate goals.</p>
    </div>
  </div>
  <div class="photo" role="img" aria-label="Video still of a realtor meeting a client at a cafe table">
    <span class="play"><svg width="16" height="18" viewBox="0 0 16 18"><path d="M2 1l13 8-13 8z" fill="#1f1a17"/></svg></span>
  </div>
</section>

<section class="team">
  <h2>Meet Our Team</h2>
  <p class="lead">Lorem ipsum dolor sit amet, consectetur adipiscing elit.</p>
  <div class="team-grid">
    <article class="member">
      <div class="portrait" role="img" aria-label="Portrait of the founder and CEO"></div>
      <div>
        <h3>Marisol Keane</h3>
        <div class="role">Founder &amp; CEO</div>
        <p>With over 15 years of experience in the Denver real estate market, Marisol Keane founded Your Harbor Agent to streamline the process of finding the perfect realtor.</p>
        <div class="socials"><span></span><span></span><span class="round"></span></div>
      </div>
    </article>
    <article class="member">
      <div class="portrait" role="img" aria-label="Portrait of the chief operating officer"></div>
      <div>
        <h3>Tobias Ferrante</h3>
        <div class="role">Chief Operating Officer</div>
        <p>With a background in business management and real estate, Tobias ensures our processes are efficient and client-focused.</p>
        <div class="socials"><span></span><span></span><span class="round"></span></div>
      </div>
    </article>
    <article class="member">
      <div class="portrait" role="img" aria-label="Portrait of the head of client services"></div>
      <div>
        <h3>Lena Okafor</h3>
        <div class="role">Head of Client Services</div>
        <p>Lena's extensive experience in customer service and real estate allows her to effectively connect clients with their ideal realtors and ensure a seamless experience.</p>
        <div class="socials"><span></span><span></span><span class="round"></span></div>
      </div>
    </article>
    <article class="member">
      <div class="portrait" role="img" aria-label="Portrait of the marketing director"></div>
      <div>
        <h3>Arjun Whitcombe</h3>
        <div class="role">Marketing Director</div>
        <p>Arjun utilizes his deep understanding of digital marketing and the real estate industry to promote Your Harbor Agent. His innovative strategies and campaigns reach and engage a broader audience.</p>
        <div class="socials"><span></span><span></span><span class="round"></span></div>
      </div>
    </article>
  </div>
</section>

<footer class="site-footer">
  <div class="brand">Your Harbor Agent</div>
  <div class="quick">
    <h4>Quick Links</h4>
    <ul><li>About Us</li><li>How it Works</li><li>Blog</li><li>Contact Us</li></ul>
  </div>
  <div class="subscribe">
    <h4>Subscribe</h4>
    <p>Join our newsletter to stay up to date on features and releases.</p>
    <div class="form-row"><div class="email">Enter your email</div><div class="btn-outline">Subscribe</div></div>
    <p class="fine">By subscribing you agree to with our <u>Privacy Policy</u> and provide consent to receive updates from our company.</p>
  </div>
  <div class="rule"></div>
  <div class="legal"><span>© 2024 Your Harbor Agent. All rights reserved.</span><u>Privacy Policy</u><u>Terms of Service</u><u>Cookies Settings</u></div>
  <div class="foot-social"><span></span><span class="sq"></span><span></span><span class="sq"></span><span class="sq"></span></div>
</footer>

</body>
</html>
```